Brightpath Holdings Business Card

Create a two sided, high gloss, quality business card for Brightpath Holdings.

Target Market(s)

People wanting to purchase, scale, and sell businesses.

Industry/Entity Type

Entrepreneurs

Contact Information for Business Card

One line: Dana Corwell, CPA, CMA Another line: Entrepreneur & Investor Another line: Business Ownership Transition Expert Another line: Multi-State Licensed Real Estate Broker Phone 954-BRTPATH (278-7284) Email Dana@Brightpath Holdings.com Website www.Brightpath.com

Requirements
Must have
• Black Card, logo on one side, all other information on the other side including a small logo.
Nice to have
• Possibly add a tagline "Helping entrepreneurs live a life they don't need a vacation from"
Should not have
• There will not be a mailing address on these cards.

```html
<!DOCTYPE html>
<html lang="en">
<head>
<meta charset="UTF-8">
<title>Brightpath Holdings – Business Card</title>
<link rel="stylesheet" href="https://fonts.googleapis.com/css2?family=Montserrat:wght@400;500;600;700;800&display=swap">
<style>
  :root {
    --bg: #3a3a3c;
    --card: #161616;
    --card-edge: #0c0c0c;
    --gold: #d8ad45;
    --white: #f2f2f2;
    --emboss: #262626;
    --emboss-hi: #2f2f2f;
  }
  * { box-sizing: border-box; margin: 0; padding: 0; }
  html, body { width: 1200px; height: 1200px; overflow: hidden; }
  body {
    background: var(--bg);
    font-family: "Montserrat", sans-serif;
    position: relative;
  }
  .card {
    position: absolute;
    left: 220px;
    width: 760px;
    height: 434px;
    border-radius: 34px;
    background: linear-gradient(160deg, #1d1d1d 0%, var(--card) 55%, var(--card-edge) 100%);
    border-bottom: 3px solid var(--gold);
    box-shadow: 0 14px 30px rgba(0,0,0,.45);
    overflow: hidden;
  }
  .card--front { top: 130px; }
  .card--back { top: 640px; }

  /* brand lockup */
  .brand {
    position: absolute;
    display: flex;
    align-items: center;
    gap: 12px;
    color: var(--gold);
    font-weight: 700;
    white-space: nowrap;
  }
  .brand__dot {
    width: 22px; height: 22px;
    border-radius: 50%;
    background: var(--gold);
    flex: none;
  }
  .card--front .brand { left: 150px; top: 84px; font-size: 40px; }

  /* contact block */
  .contact {
    position: absolute;
    left: 410px;
    top: 168px;
    list-style: none;
    color: var(--white);
    font-size: 18px;
    font-weight: 500;
    line-height: 1;
  }
  .contact li {
    display: flex;
    align-items: center;
    gap: 10px;
    margin-bottom: 14px;
  }
  .contact svg { width: 18px; height: 18px; flex: none; }

  /* identity block */
  .identity {
    position: absolute;
    left: 40px;
    bottom: 40px;
    color: var(--white);
  }
  .identity__name {
    color: var(--gold);
    font-size: 34px;
    font-weight: 700;
    letter-spacing: 1px;
    margin-bottom: 6px;
  }
  .identity__line {
    font-size: 12.5px;
    font-weight: 500;
    letter-spacing: .3px;
    line-height: 1.3;
    text-transform: uppercase;
  }

  /* back pattern */
  .pattern { position: absolute; inset: 0; }
  .card--back .brand {
    font-size: 26px;
    gap: 10px;
  }
  .card--back .brand__dot { width: 14px; height: 14px; }
  .pattern .brand {
    color: var(--emboss-hi);
    text-shadow: 0 1px 0 #0a0a0a;
  }
  .pattern .brand__dot { background: var(--emboss); }
  .card--back .brand--feature {
    left: 230px; top: 196px;
    color: var(--gold);
  }
</style>
</head>
<body>

<section class="card card--front" aria-label="Card front">
  <div class="brand"><span class="brand__dot"></span>Brightpath Holdings</div>

  <ul class="contact">
    <li>
      <svg viewBox="0 0 24 24" aria-hidden="true"><path fill="#d8ad45" d="M6.6 10.8a15.1 15.1 0 0 0 6.6 6.6l2.2-2.2c.3-.3.7-.4 1-.2 1.1.4 2.3.6 3.6.6.6 0 1 .4 1 1V20c0 .6-.4 1-1 1A17 17 0 0 1 3 4c0-.6.4-1 1-1h3.5c.6 0 1 .4 1 1 0 1.3.2 2.5.6 3.6.1.3 0 .7-.2 1z"/></svg>
      954-BRTPATH (278-7284)
    </li>
    <li>
      <svg viewBox="0 0 24 24" aria-hidden="true"><g fill="none" stroke="#d8ad45" stroke-width="1.8"><circle cx="12" cy="12" r="9"/><ellipse cx="12" cy="12" rx="4" ry="9"/><path d="M3 12h18M5 7h14M5 17h14"/></g></svg>
      www.Brightpath.com
    </li>
    <li>
      <svg viewBox="0 0 24 24" aria-hidden="true"><rect x="2" y="5" width="20" height="14" rx="1.5" fill="#d8ad45"/><path d="M3 6l9 7 9-7" fill="none" stroke="#161616" stroke-width="1.6"/></svg>
      Dana@BrightpathHoldings.com
    </li>
  </ul>

  <div class="identity">
    <h1 class="identity__name">DANA CORWELL</h1>
    <p class="identity__line">CPA, CMA, Entrepreneur, Investor</p>
    <p class="identity__line">Business Ownership Transition Expert</p>
    <p class="identity__line">Multi-State Licensed Real Estate Broker</p>
  </div>
</section>

<section class="card card--back" aria-label="Card back">
  <div class="pattern" aria-hidden="true">
    <div class="brand" style="left:40px;top:30px"><span class="brand__dot"></span>Brightpath Holdings</div>
    <div class="brand" style="left:400px;top:30px"><span class="brand__dot"></span>Brightpath Holdings</div>
    <div class="brand" style="left:40px;top:112px"><span class="brand__dot"></span>Brightpath Holdings</div>
    <div class="brand" style="left:400px;top:112px"><span class="brand__dot"></span>Brightpath Holdings</div>
    <div class="brand" style="left:40px;top:280px"><span class="brand__dot"></span>Brightpath Holdings</div>
    <div class="brand" style="left:400px;top:280px"><span class="brand__dot"></span>Brightpath Holdings</div>
    <div class="brand" style="left:40px;top:360px"><span class="brand__dot"></span>Brightpath Holdings</div>
    <div class="brand" style="left:400px;top:360px"><span class="brand__dot"></span>Brightpath Holdings</div>
  </div>
  <div class="brand brand--feature"><span class="brand__dot"></span>Brightpath Holdings</div>
</section>

</body>
</html>
```